Rehab/fitness Business card design

I need a design that promotes "A peak ridge base for movers". services include assessment, massage, physiotherapy, pilates, suspension training, kinesiotaping in any combination.
I would like to bring the design into my website, flyers etc

Target Market(s)

athletes from beginner to elite - any age, male and female

Industry/Entity Type

Shop

Contact Information for Business Card

Peak-Ridge-Base for Movers
17 Halden Rise, Larchvale, Kessington
027 418 7093
kerry.dunlow@vestmail.test

Logo Text

Logo styles of interest
Abstract Logo
Requirements
Nice to have
• Blue colour theme

```html
<!DOCTYPE html>
<html lang="en">
<head>
<meta charset="utf-8">
<title>Peak-Ridge-Base for Movers — Business Card</title>
<link rel="stylesheet" href="https://fonts.googleapis.com/css2?family=Open+Sans:wght@400;600&display=swap">
<style>
  :root {
    --page-bg: #2b2b2d;
    --card-deep: #0d1f55;
    --card-mid: #1b3f8c;
    --card-light: #7f9cc9;
    --band-blue: #1f57a8;
    --text-white: #ffffff;
    --text-soft: #f2f5fb;
  }
  * { margin: 0; padding: 0; box-sizing: border-box; }
  html, body {
    width: 1200px;
    height: 1000px;
    overflow: hidden;
    background: var(--page-bg);
    font-family: "Open Sans", Arial, sans-serif;
  }
  .business-card {
    position: absolute;
    left: 232px;
    top: 283px;
    width: 708px;
    height: 388px;
    overflow: hidden;
    background: var(--card-deep);
  }
  .card-texture {
    position: absolute;
    inset: 0;
    background:
      radial-gradient(ellipse 360px 220px at 300px 60px, var(--card-light) 0%, rgba(127,156,201,0.4) 45%, rgba(127,156,201,0) 100%),
      radial-gradient(ellipse 260px 300px at 120px 300px, rgba(27,63,140,0.9) 0%, rgba(27,63,140,0) 100%),
      linear-gradient(120deg, var(--card-mid) 0%, #173a86 40%, var(--card-deep) 100%);
  }
  .brand-band {
    position: absolute;
    left: 0;
    top: 71px;
    width: 402px;
    height: 70px;
    background: var(--band-blue);
    opacity: 0.92;
  }
  .brand-name {
    position: absolute;
    left: 30px;
    top: 12px;
    width: 345px;
    color: var(--text-white);
    font-weight: 600;
    text-transform: uppercase;
    line-height: 1;
  }
  .brand-name .brand-main {
    display: block;
    font-size: 29px;
    letter-spacing: 4.4px;
    white-space: nowrap;
  }
  .brand-name .brand-sub {
    display: block;
    font-size: 12.5px;
    letter-spacing: 4px;
    text-align: right;
    margin-top: 3px;
    margin-right: -4px;
  }
  .contact-list {
    position: absolute;
    left: 436px;
    top: 82px;
    list-style: none;
    color: var(--text-soft);
    font-size: 13.5px;
    line-height: 18px;
    white-space: nowrap;
  }
  .services-line {
    position: absolute;
    left: 0;
    right: 0;
    bottom: 13px;
    text-align: center;
    color: var(--text-white);
    font-size: 12.7px;
    text-transform: uppercase;
    white-space: nowrap;
  }
</style>
</head>
<body>
  <div class="business-card">
    <div class="card-texture" role="img" aria-label="Weathered blue grunge wall texture"></div>
    <div class="brand-band">
      <div class="brand-name">
        <span class="brand-main">Peak-Ridge-Base</span>
        <span class="brand-sub">for Movers</span>
      </div>
    </div>
    <ul class="contact-list">
      <li>T: 027 418 7093</li>
      <li>A: 17 Halden Rise, Larchvale, Kessington</li>
      <li>E: kerry.dunlow@vestmail.test</li>
    </ul>
    <p class="services-line">Assessment, Massage, Physiotherapy Pilates, Suspension Training, Kinesiotaping in any combination</p>
  </div>
</body>
</html>
```